Cover Page Design

Create a new cover page in a sleek modern look that consists of our logo as provided. This cover page will be used in presentations and should only have colors featured in our branding efforts.

Target Market(s)

Architectural and Interior Design Clients

Industry/Entity Type

Interior Design

Font styles to use
Other font styles liked:
• see attached logo

Colors

Designer to choose colors to be used in the design.

Requirements
Must have
• Clean look, no pictures. just logo.
Nice to have
• colors that relate to our brand.
Should not have
• No colors not featured in our branding:
• www.veltamarsh.com

```html
<!DOCTYPE html>
<html lang="en">
<head>
<meta charset="utf-8">
<title>Velta Marsh + Partners — Presentation Cover</title>
<link href="https://fonts.googleapis.com/css2?family=Montserrat:wght@400&display=swap" rel="stylesheet">
<style>
  :root {
    --brand-blue: #0072bc;
    --brand-grey: #a3a4a8;
    --ink: #231f20;
    --paper: #ffffff;
  }
  html, body {
    margin: 0;
    padding: 0;
    overflow: hidden;
    background: var(--paper);
  }
  .cover {
    position: relative;
    width: 1200px;
    height: 725px;
    background: var(--paper);
    overflow: hidden;
  }
  .cover__stripes {
    position: absolute;
    left: 0;
    top: 0;
    width: 1200px;
    height: 725px;
  }
  .stripe--blue { fill: var(--brand-blue); }
  .stripe--grey { fill: var(--brand-grey); }
  .brand-dot { fill: var(--brand-blue); }
  .brand {
    position: absolute;
    left: 845px;
    top: 543px;
    width: 304px;
    font-family: "Montserrat", sans-serif;
    font-weight: 400;
    color: var(--ink);
    text-align: right;
  }
  .brand__name {
    margin: 0;
    font-size: 31px;
    line-height: 36px;
    letter-spacing: 1.5px;
    white-space: nowrap;
  }
  .brand__suffix {
    margin: 3px 0 0;
    font-size: 9px;
    line-height: 12px;
    letter-spacing: 0.9em;
    margin-right: -0.9em;
    white-space: nowrap;
  }
</style>
</head>
<body>
  <main class="cover">
    <svg class="cover__stripes" viewBox="0 0 1200 725" aria-hidden="true">
      <polygon class="stripe--blue" points="0,527 734,527 732,530 0,530"/>
      <polygon class="stripe--blue" points="0,547 723,547 722,550 0,550"/>
      <polygon class="stripe--grey" points="0,567 719,567 719,570 0,570"/>
      <polygon class="stripe--blue" points="0,587 722,587 723,590 0,590"/>
      <polygon class="stripe--blue" points="0,607 732,607 734,610 0,610"/>
      <circle class="brand-dot" cx="788" cy="568" r="42"/>
    </svg>
    <div class="brand">
      <p class="brand__name">VELTA MARSH</p>
      <p class="brand__suffix">+ PARTNERS</p>
    </div>
  </main>
</body>
</html>
```